Label for honey jars and buckets

My mom needs a label for her honey. The company is called 'Cedar Hollow Apiary' It needs to say 'Raw Fireweed Honey' somewhere on the label and then in small print Fernvale, WC with this phone number underneath 250-417-3862. There needs to be 3 sizes of the same label the 1) width 2 inches x height 2 3/4 inches 2) width 5 inches x height 3 inches 3) 2 3/4 inches round label

She really liked the first bee and honeycomb logo you did for my lotion label, the one with the white bee and yellow honeycomb, so something like that would be great. I've uploaded a few pictures of her bees and a picture of the fireweed flower that the bees make the honey from to give you some ideas.

It needs to have an artisan feel, it is a small company that's locally owned and operated.
Updates

I was thinking that having some mountain ranges worked into the background of the label would look nice and be really fitting, the picture of the fireweed that I uploaded has a good example of the types on mountains in the area. 

Industry/Entity Type

It Company

Requirements
Should not have
• Not too many colours

```html
<!DOCTYPE html>
<html lang="en">
<head>
<meta charset="utf-8">
<title>Cedar Hollow Apiary – Honey Labels</title>
<link rel="stylesheet" href="https://fonts.googleapis.com/css2?family=Cormorant+Garamond:wght@500&family=Delius&family=Roboto+Condensed:wght@400&display=swap">
<style>
  :root {
    --paper: #ffffff;
    --honey: #f5c211;
    --honey-deep: #d4a90c;
    --gold-type: #c9a10a;
    --slate: #4a4f58;
    --trim: #5ee6ee;
  }
  html, body {
    margin: 0;
    padding: 0;
    width: 1200px;
    height: 1000px;
    overflow: hidden;
    background: var(--paper);
  }
  .label-sheet { display: block; width: 1200px; height: 1000px; }
  .trim-line { fill: var(--paper); stroke: var(--trim); stroke-width: 1; }
  .comb-band { fill: url(#combFill); }
  .bee-art { fill: url(#beeFill); }
  .brand-serif {
    font-family: "Cormorant Garamond", Georgia, serif;
    font-weight: 500;
    fill: var(--slate);
    text-anchor: middle;
  }
  .brand-script {
    font-family: "Delius", "Comic Sans MS", cursive;
    fill: var(--gold-type);
    text-anchor: middle;
  }
  .product-name {
    font-family: "Delius", "Comic Sans MS", cursive;
    fill: var(--slate);
    text-anchor: middle;
  }
  .contact-line {
    font-family: "Roboto Condensed", "Arial Narrow", sans-serif;
    fill: var(--slate);
    text-anchor: middle;
  }
</style>
</head>
<body>
<svg class="label-sheet" viewBox="0 0 1200 1000" xmlns="http://www.w3.org/2000/svg">
  <defs>
    <linearGradient id="combFill" x1="0" y1="0" x2="0" y2="1">
      <stop offset="0" stop-color="#f5c211"/>
      <stop offset="0.5" stop-color="#e9b70f"/>
      <stop offset="1" stop-color="#f5c211"/>
    </linearGradient>
    <radialGradient id="beeFill">
      <stop offset="0" stop-color="#e0a516"/>
      <stop offset="1" stop-color="#fbeeb8"/>
    </radialGradient>
    <clipPath id="wideClip"><rect x="290" y="118" width="590" height="352" rx="8"/></clipPath>
    <clipPath id="roundClip"><circle cx="390" cy="726" r="190"/></clipPath>
    <clipPath id="tallClip"><rect x="738" y="540" width="255" height="348" rx="14"/></clipPath>
  </defs>

  <!-- Wide label 5 x 3 -->
  <g class="label label-wide">
    <rect class="trim-line" x="290" y="118" width="590" height="352" rx="8"/>
    <g clip-path="url(#wideClip)">
      <polygon class="comb-band" role="img" aria-label="Honeycomb decoration" points="290,118 410,118 500,232 410,326 412,470 290,470"/>
      <polygon class="comb-band" role="img" aria-label="Honeycomb decoration" points="880,118 762,118 674,232 762,326 762,470 880,470"/>
    </g>
    <ellipse class="bee-art" role="img" aria-label="Honey bee illustration" cx="580" cy="176" rx="36" ry="26"/>
    <text class="brand-serif" x="583" y="256" font-size="46">CEDAR HOLLOW</text>
    <text class="brand-script" x="583" y="310" font-size="56">Apiary</text>
    <text class="product-name" x="583" y="374" font-size="35">Raw Fireweed Honey</text>
    <text class="contact-line" x="583" y="421" font-size="28">Fernvale, WC • 250-417-3862</text>
  </g>

  <!-- Round label 2 3/4 -->
  <g class="label label-round">
    <circle class="trim-line" cx="390" cy="726" r="190"/>
    <g clip-path="url(#roundClip)">
      <polygon class="comb-band" role="img" aria-label="Honeycomb decoration" points="195,580 262,580 290,680 262,780 195,780"/>
      <polygon class="comb-band" role="img" aria-label="Honeycomb decoration" points="585,580 518,580 490,680 518,780 585,780"/>
    </g>
    <ellipse class="bee-art" role="img" aria-label="Honey bee illustration" cx="385" cy="583" rx="33" ry="24"/>
    <text class="brand-serif" x="390" y="660" font-size="42">CEDAR</text>
    <text class="brand-serif" x="390" y="705" font-size="42">HOLLOW</text>
    <text class="brand-script" x="390" y="776" font-size="60">Apiary</text>
    <text class="product-name" x="390" y="828" font-size="30">Raw Fireweed Honey</text>
    <text class="contact-line" x="390" y="861" font-size="24">Fernvale, WC</text>
    <text class="contact-line" x="390" y="890" font-size="24">250-417-3862</text>
  </g>

  <!-- Tall label 2 x 2 3/4 -->
  <g class="label label-tall">
    <rect class="trim-line" x="738" y="540" width="255" height="348" rx="14"/>
    <g clip-path="url(#tallClip)">
      <polygon class="comb-band" role="img" aria-label="Honeycomb decoration" points="738,565 766,565 790,645 766,723 738,723"/>
      <polygon class="comb-band" role="img" aria-label="Honeycomb decoration" points="993,565 964,565 940,645 964,723 993,723"/>
    </g>
    <ellipse class="bee-art" role="img" aria-label="Honey bee illustration" cx="850" cy="588" rx="32" ry="23"/>
    <text class="brand-serif" x="866" y="652" font-size="36">CEDAR</text>
    <text class="brand-serif" x="866" y="693" font-size="36">HOLLOW</text>
    <text class="brand-script" x="866" y="763" font-size="56">Apiary</text>
    <text class="product-name" x="866" y="806" font-size="25">Raw Fireweed Honey</text>
    <text class="contact-line" x="866" y="843" font-size="22">Fernvale, WC</text>
    <text class="contact-line" x="866" y="870" font-size="22">250-417-3862</text>
  </g>
</svg>
</body>
</html>
```